Willow Crest Website

We need a website that has clean, asian looking images that relax and motivate people to come into our integrated medical center. My current website is www.pinebrookcare.example and I would like the design for Willow Crest Health Solutions to be similar but more inviting with video content and a product purchase store as well. A moving banner would be nice too. When people are looking for ways of losing weight or getting out of pain we want them to make the connection that we have the solution. This website needs to provide sufficient information so that patients are well informed and choose us as their health provider before they ever walk through our doors. We offer comprehensive natural medicine that is based on the principles that the body can heal itself when given the right conditions. Our services include medical weight loss and hormone balancing, acupuncture and chinese herbal medicine, physical medicine, trigger point injections, allergy testing and joint rehabilitation. The Medical Doctor and Licensed Acupuncturist work as a team to provide optimal care that is catered to each individual who comes through our doors.
Updates

Target Market(s)

40 to 50 year olds who want to lose weight or have pain issues.

Industry/Entity Type

Medical

Requirements
Must have
• Use photos from our website www.pinebrookcare.example or similar content. Video content. Moving banner with relaxing images.
Nice to have
• Happy, healthy looking people. Medical Doctors working as a team. Friendly staff in a cutting edge facility.
Should not have
• Papyrus font, or big bold words.

```html
<!DOCTYPE html>
<html lang="en">
<head>
<meta charset="utf-8">
<title>Willow Crest Acupuncture</title>
<link rel="stylesheet" href="https://fonts.googleapis.com/css2?family=Ubuntu+Condensed&family=Ubuntu:wght@300;400;500&display=swap">
<style>
:root{
  --olive:#5d5a23;
  --olive-mark:#6a6327;
  --orange:#c9561f;
  --orange-dark:#9f4418;
  --rust:#a64a1c;
  --text:#4a4a4a;
  --white:#ffffff;
  --green:#6a9a3c;
  --condensed:"Ubuntu Condensed","Ubuntu",sans-serif;
}
*{box-sizing:border-box;margin:0;padding:0}
html,body{width:1029px;height:1200px;overflow:hidden}
body{background:var(--olive);font-family:"Ubuntu",sans-serif;color:var(--text);position:relative}
.topbar{position:absolute;left:0;top:0;width:1029px;height:30px;background:linear-gradient(#ffffff,#ececec);border-bottom:1px solid #d8d8d8}
.phones{position:absolute;right:105px;top:7px;font-size:14px;color:#444}
.page{position:absolute;left:94px;top:30px;width:841px;height:1170px;background:var(--white)}
.abs{position:absolute}
.connect{right:222px;top:40px;font-size:17px;line-height:22px;color:#666;font-style:italic;font-weight:300;white-space:nowrap}
.connect b{font-style:normal;font-weight:500;color:var(--olive-mark)}
.social{top:40px;width:22px;height:22px;border-radius:50%}
.brand{left:117px;top:0;width:103px;height:161px;background:var(--olive-mark);color:#fff;display:flex;align-items:center;justify-content:center;text-align:center;font-size:15px;font-weight:500;letter-spacing:2px;line-height:1.4;z-index:3}
.nav{left:103px;top:70px;width:823px;height:37px;background:linear-gradient(#d8682b,var(--orange) 60%,#b54b1a);border-radius:6px 6px 0 0;z-index:2}
.nav a{position:absolute;top:0;height:37px;line-height:38px;color:#fff;text-decoration:none;font-family:var(--condensed);font-size:12.5px;transform:translateX(-50%);white-space:nowrap}
.nav i{position:absolute;top:0;width:1px;height:37px;background:#a84516;box-shadow:1px 0 0 #e07a43}
.hero{left:103px;top:107px;width:823px;height:330px}
.quote{left:117px;top:191px;width:280px;font-size:14.3px;line-height:20.5px;font-weight:300;color:#333}
.author{left:293px;top:289px;font-size:12.5px;color:var(--rust)}
.dot{top:383px;width:8px;height:8px;border-radius:50%;background:#444}
.dot.on{background:var(--orange);box-shadow:0 0 0 2px #fff,0 0 0 3px var(--orange)}
.card{top:443px;width:255px;height:187px;border:1px solid #ddd;background:linear-gradient(#fff 60%,#ececec);box-shadow:0 1px 3px rgba(0,0,0,.12)}
.card .shot{position:absolute;left:5px;top:5px;width:243px;height:92px;border-radius:3px}
.card h3{position:absolute;left:8px;top:105px;font-family:var(--condensed);font-weight:400;font-size:16px;color:var(--orange-dark)}
.card p{position:absolute;left:8px;top:124px;width:240px;font-size:9.6px;line-height:15.4px;color:#666}
.more{width:106px;height:22px;border-radius:11px;background:linear-gradient(#da6a2e,var(--orange-dark));color:#fff;font-family:var(--condensed);font-size:10.5px;text-align:center;line-height:22px;top:621px;box-shadow:0 3px 3px rgba(0,0,0,.15)}
.welcome{left:111px;top:659px;font-size:21px;font-weight:300;color:#222}
.welcome span{color:var(--rust);font-weight:400}
.sub{left:114px;top:692px;font-size:13px;color:var(--olive-mark);font-weight:400}
.body{left:114px;top:733px;width:515px;font-size:10px;line-height:20.6px;color:#444}
.ftitle{left:663px;top:660px;font-size:17.5px;color:var(--rust)}
.vbox{left:656px;top:689px;width:267px;height:185px;border:1px solid #ddd}
.vshot{left:662px;top:694px;width:256px;height:143px}
.vlib{left:662px;top:846px;font-size:11.5px;line-height:11px;color:#888;font-weight:300}
.vlib small{display:block;font-size:8.5px;color:var(--green);font-weight:500}
.vbtn{left:759px;top:846px;width:159px;height:22px;border-radius:3px;background:linear-gradient(#82b04f,#5a8a2e);color:#fff;font-size:8px;line-height:22px;padding-left:9px}
.ptitle{left:117px;top:877px;font-size:16.5px;color:var(--orange)}
.prod{top:910px;width:179px;height:204px;border:1px solid #e3e3e3;background:#fff}
.prod .shot{position:absolute;left:8px;top:8px;width:162px;height:110px}
.prod .sep{position:absolute;left:0;right:0;top:127px;border-top:1px solid #e6e6e6}
.prod h4{position:absolute;left:9px;top:134px;font:500 10.5px Arial,sans-serif;color:#777}
.prod .desc{position:absolute;left:9px;top:147px;font:9.5px Arial,sans-serif;color:#aaa}
.prod .price{position:absolute;left:9px;top:169px;font-family:Georgia,serif;font-style:italic;font-size:16px;color:var(--rust)}
.prod .cart{position:absolute;left:97px;top:170px;width:72px;height:24px;border-radius:3px;background:linear-gradient(#d7652a,var(--orange-dark));color:#f6dccd;font-size:9.5px;text-align:center;line-height:24px}
.footer{left:94px;top:1151px;width:841px;height:49px;background:var(--orange)}
.flinks{left:114px;top:1160px;font-size:10.8px;color:#fff}
.flinks b{font-weight:300;margin:0 7px}
.copy{left:113px;top:1180px;font-size:9px;color:#fde6d8}
</style>
</head>
<body>
<div class="topbar"><div class="phones">(555) 214-0190 &nbsp;OR &nbsp;(555) 386-2271</div></div>
<div class="page"></div>

<div class="abs connect">let’s stay <b>Connected!</b></div>
<span class="abs social" style="left:815px;background:#2d63b2" aria-label="Social link"></span>
<span class="abs social" style="left:842px;background:#3fa9e0" aria-label="Social link"></span>
<span class="abs social" style="left:869px;background:#1f6aa8" aria-label="Social link"></span>
<span class="abs social" style="left:896px;background:#e7781f" aria-label="Social link"></span>

<div class="abs brand">WILLOW<br>CREST</div>

<nav class="abs nav">
  <a style="left:169px">SO TAI HO</a><i style="left:216px"></i>
  <a style="left:266px">SEITAI SHINPO</a><i style="left:320px"></i>
  <a style="left:375px">ACUPUNCTURE</a><i style="left:430px"></i>
  <a style="left:477px">BIOGRAPHY</a><i style="left:524px"></i>
  <a style="left:568px">NUTRITION</a><i style="left:613px"></i>
  <a style="left:661px">MY JOURNEY</a><i style="left:709px"></i>
  <a style="left:760px">CONTANT US</a>
</nav>

<svg class="abs hero" viewBox="0 0 823 330">
  <defs>
    <clipPath id="heroShape"><path d="M1 0H822V295Q420 352 1 295Z"/></clipPath>
    <linearGradient id="heroPhoto" x1="0" x2="1" y1="0" y2="0">
      <stop offset="0" stop-color="#ffffff"/>
      <stop offset=".35" stop-color="#e9c3a4"/>
      <stop offset=".7" stop-color="#f0cdb2"/>
      <stop offset="1" stop-color="#f7e6da"/>
    </linearGradient>
  </defs>
  <g clip-path="url(#heroShape)">
    <rect x="330" y="0" width="493" height="330" fill="url(#heroPhoto)" role="img" aria-label="Photo of a smiling woman relaxing during a spa treatment"/>
  </g>
  <path d="M1 0V295Q420 352 822 295V0" fill="none" stroke="#c9561f" stroke-width="1.5"/>
</svg>
<p class="abs quote">"The Doctor of the future will give no medi-cine but will interest patients in the care of the human frame, in diet, and &nbsp;in the cause and prevention of disease."</p>
<div class="abs author">Arthur Penwell</div>
<span class="abs dot on" style="left:119px"></span>
<span class="abs dot" style="left:138px"></span>
<span class="abs dot" style="left:157px"></span>
<span class="abs dot" style="left:177px"></span>

<div class="abs card" style="left:114px">
  <div class="shot" role="img" aria-label="Photo of a shoulder massage" style="background:linear-gradient(90deg,#f3ddcd,#d9ab8a 50%,#f6e6da)"></div>
  <h3>SO THI HO</h3>
  <p>Sotai ho is a system of movement therapy that was discovered after nearly 10 years of personal research from Kenji Harada, M.D. (1897-1993)</p>
</div>
<div class="abs card" style="left:388px">
  <div class="shot" role="img" aria-label="Photo of an acupuncture treatment" style="background:linear-gradient(90deg,#dfe7ee,#e8cbb4 55%,#f2f2f2)"></div>
  <h3>SEITAI SHINPO</h3>
  <p>Seitai Shinpo is a system of acupuncture developed by Dr. Hiro Tanabe in the 1970s. He was the first to discover that internal organ systems ..</p>
</div>
<div class="abs card" style="left:662px">
  <div class="shot" role="img" aria-label="Photo of a back treatment in a clinic" style="background:linear-gradient(90deg,#eef0f0,#e6bf9f 45%,#f3e3d6)"></div>
  <h3>ACUPUNCTURE</h3>
  <p>While pursuing a degree in premedicine &amp; behavior science at the State U, Marin learned the benefits of Chinese medicine</p>
</div>
<div class="abs more" style="left:176px">Read More</div>
<div class="abs more" style="left:449px">Read More</div>
<div class="abs more" style="left:724px">Read More</div>

<h1 class="abs welcome">Welcome to <span>Willow Crest Acupuncture</span></h1>
<h2 class="abs sub">How does acupuncture work?</h2>
<p class="abs body">As the needles are carefully inserted into acupuncture points, specific cells stimulate nerve pathways that trigger a healing response to a particular organ system or area of the body. &nbsp;Acupuncture also acts on the auto-nomic nervous system and causes the release of endorphins, enkephalins and other natural pain relieving chemicals. &nbsp;At Willow Crest Acupuncture the system of acupuncture used is called Seitai Shinpo (which translates into “correct posture acupuncture method”) that uses acupuncture and moxibustion to balance structural distortions by releasing tense areas of contraction along the spine. &nbsp;When the structure is properly balanced</p>

<div class="abs ftitle">Featured Video</div>
<div class="abs vbox"></div>
<div class="abs vshot" role="img" aria-label="Video still of a relaxing herbal spa massage" style="background:linear-gradient(120deg,#8a5a34,#d8a47c 45%,#6e7a3a)"></div>
<svg class="abs" style="left:671px;top:800px" width="240" height="28" viewBox="0 0 240 28">
  <rect x="0" y="0" width="42" height="28" rx="3" fill="#222" opacity=".85"/>
  <path d="M16 7L28 14L16 21Z" fill="#fff"/>
  <rect x="48" y="6" width="190" height="18" rx="3" fill="#222" opacity=".85"/>
  <text x="56" y="18" font-size="7" fill="#ddd" font-family="Arial, sans-serif">00:00</text>
  <rect x="80" y="11" width="102" height="6" fill="none" stroke="#aaa"/>
  <rect x="187" y="11" width="32" height="6" fill="#8c8"/>
  <path d="M225 10h4M225 10v4M234 20h-4M234 20v-4" stroke="#fff" stroke-width="1.5"/>
</svg>
<div class="abs vlib">VIDEO LIBRARY<small>GET TO KNOW US</small></div>
<div class="abs vbtn">CLICK HERE FOR MORE VIDEOS
  <svg style="position:absolute;right:8px;top:5px" width="16" height="12" viewBox="0 0 16 12"><rect x="1" y="1" width="14" height="8" fill="none" stroke="#fff" stroke-width="1.4"/><path d="M5 11h6" stroke="#fff" stroke-width="1.4"/></svg>
</div>

<div class="abs ptitle">Our Products</div>
<div class="abs prod" style="left:116px">
  <div class="shot" role="img" aria-label="Photo of candles and white towels" style="background:linear-gradient(135deg,#4d6a33,#e9ebe0 50%,#a7c259)"></div>
  <div class="sep"></div><h4>Lorem ipsum dolor sit ame</h4><div class="desc">Consectetuer elit....</div>
  <div class="price">$30.99</div><div class="cart">Add to cart</div>
</div>
<div class="abs prod" style="left:320px">
  <div class="shot" role="img" aria-label="Photo of lavender, lemon and essential oil" style="background:linear-gradient(135deg,#c9b48d,#d7c96a 50%,#8a7aa8)"></div>
  <div class="sep"></div><h4>Lorem ipsum dolor sit ame</h4><div class="desc">Consectetuer elit....</div>
  <div class="price">$25.99</div><div class="cart">Add to cart</div>
</div>
<div class="abs prod" style="left:521px">
  <div class="shot" role="img" aria-label="Photo of candles, flowers and towels" style="background:linear-gradient(135deg,#4a2a1a,#e6d6c0 50%,#c2491f)"></div>
  <div class="sep"></div><h4>Lorem ipsum dolor sit ame</h4><div class="desc">Consectetuer elit....</div>
  <div class="price">$35.99</div><div class="cart">Add to cart</div>
</div>
<div class="abs prod" style="left:722px">
  <div class="shot" role="img" aria-label="Photo of a flower and a wooden oil bowl" style="background:linear-gradient(135deg,#f2efe0,#6f8a3a 45%,#b06a2a)"></div>
  <div class="sep"></div><h4>Lorem ipsum dolor sit ame</h4><div class="desc">Consectetuer elit....</div>
  <div class="price">$50.99</div><div class="cart">Add to cart</div>
</div>

<footer class="abs footer"></footer>
<div class="abs flinks">So Tai Ho<b>|</b>Seitai Shinpo<b>|</b>Acupuncture<b>|</b>Biography<b>|</b>Nutrition<b>|</b>My Journey<b>|</b>Contact Us</div>
<div class="abs copy">Copyright 2012 © Willow Crest Acupuncture — All Rights Reserved</div>
</body>
</html>
```